Natural Organic soap need packaging design

we need a packaging design for new company based in New Zealand Called 'Bremta Global ltd'.. We manufacture Natural organic soap bars.our main USP is that this soap is made of all natural ingredient and no chemical used and soap is made in New Zealand,so we need a design which look natural,simple,classy and luxury and packaging should reflect that its made in New Zealand.please find attached photos of sample soap.
soap will be in two variant:
1. Pure Manuka Honey soap
2. Goat Milk soap
NOTE: the soap in picture is not actually our soap its just a sample what our soap will look like so please don't make a design with KLOMPP written on it. BREMTA is the soap name.
Target Market(s)
international market. mainly young and kids
Industry/Entity Type
It Company

```html
<!DOCTYPE html>
<html lang="en">
<head>
<meta charset="utf-8">
<title>Bremta Goat Milk Soap – Label</title>
<link rel="stylesheet" href="https://fonts.googleapis.com/css2?family=Jura:wght@400;500&display=swap">
<style>
  :root {
    --canvas-bg: #ebe9ec;
    --pattern-dark: #1a1a1a;
    --pattern-light: #f4f4f4;
    --panel-pink: #ff3d6e;
    --logo-black: #111111;
    --text-white: #ffffff;
  }
  * { margin: 0; padding: 0; box-sizing: border-box; }
  html, body {
    width: 1200px;
    height: 1126px;
    overflow: hidden;
    background: var(--canvas-bg);
  }
  .canvas {
    position: relative;
    width: 1200px;
    height: 1126px;
    font-family: "Jura", sans-serif;
  }
  .label {
    position: absolute;
    left: 140px;
    top: 233px;
    width: 920px;
    height: 660px;
    box-shadow: 0 6px 24px rgba(0, 0, 0, 0.12);
  }
  .label-pattern {
    position: absolute;
    inset: 0;
    background: linear-gradient(135deg, #5e5e5e 0%, #8a8a8a 50%, #5e5e5e 100%);
  }
  .label-panel {
    position: absolute;
    left: 130px;
    top: 150px;
    width: 700px;
    height: 400px;
    background: var(--panel-pink);
  }
  .product-copy {
    position: absolute;
    left: 44px;
    bottom: 52px;
    color: var(--text-white);
  }
  .product-name {
    font-size: 66px;
    font-weight: 500;
    letter-spacing: 1px;
    line-height: 1.05;
  }
  .product-type {
    font-size: 38px;
    font-weight: 400;
    letter-spacing: 0.5px;
    margin-top: 6px;
  }
  .product-claim {
    font-size: 19px;
    font-weight: 400;
    margin-top: 10px;
    letter-spacing: 0.3px;
  }
  .brand-block {
    position: absolute;
    left: 560px;
    top: 100px;
    width: 250px;
    height: 150px;
    background: var(--logo-black);
    display: flex;
    align-items: center;
    justify-content: center;
    gap: 14px;
  }
  .brand-dot {
    width: 18px;
    height: 18px;
    border-radius: 50%;
    background: var(--text-white);
  }
  .brand-name {
    color: var(--text-white);
    font-size: 40px;
    font-weight: 500;
    letter-spacing: 3px;
  }
</style>
</head>
<body>
  <main class="canvas">
    <section class="label">
      <div class="label-pattern" role="img" aria-label="Black and white zigzag chevron pattern"></div>
      <div class="label-panel">
        <div class="product-copy">
          <h1 class="product-name">Goat Milk soap</h1>
          <p class="product-type">natural organic soap bars</p>
          <p class="product-claim">made of all natural ingredient and no chemical used</p>
        </div>
      </div>
      <div class="brand-block">
        <span class="brand-dot"></span>
        <span class="brand-name">BREMTA</span>
      </div>
    </section>
  </main>
</body>
</html>
```